【業務の内容】
建物(鉄筋(鉄骨)コンクリート躯体)の寿命が、あとどれくらい
残っているのか(=寿命)を評価する業務

【なぜこの業務が必要か】
・いまお住まいのマンションの将来計画を考えるために重要な基礎資料
例えば
・「建物寿命は、あと50年以上あるので、しっかりと設備も改修しよう」
・「建物寿命は、あと50年以上あるので、耐震補強を考えよう」
・「建物寿命が20年程度しか残っていないから、延命のための改修をしよう」
・「建物寿命が20年程度しか残っていないから、建替えの検討をしよう」
・残存寿命が長いなら、耐震補強や給排水設備の改修、共用部のリニューアル等を
実施する価値がある、と判断できる

【この業務を推す背景】
・築30年、40年を超える高経年マンションが増えてきている
・首都圏では大地震の確率が30年以内に70%と言われており。1981年以前の旧耐震
基準の建物は、すでに築40年を超えており、耐震補強工事を行うか、建替えるかの
選択を迫られている

【業務の費用(目安・税別)】 ※あくまでも目安
・1棟当たり 基本料金300,000+コア抜き50,000/ヶ所(1フロアあたり1ヶ所)

例)5階建て1棟のマンションの場合
基本料金300,000+(50,000×5ヶ所)=550,000(税別)
【訴求したい事】
・建物の寿命評価に特化しているので、耐震診断等と比べて比較的
安価に実施できる
・短期間で結果が分かる(着手後およそ1か月程度)
・これからマンションにどれだけ維持修繕や改良などの投資するかという
検討をする際の客観的裏付けのある基礎資料になる
・耐用年数は「集合住宅躯体の長期保全評価指針・同付録」(日本建築
学会)の示す算定式を使って算出する

【特に注意・留意すべき事象】
・「寿命が長い」=「安全」ではない
建物耐用年数が長くても、現在の耐震性能基準に達していなければ大地震で
大破・倒壊の危険性がある。躯体寿命と建物の安全性は全く別物
・建物の寿命と設備(給排水管や電気設備など)の寿命は別物
株式会社環創プラン 本社
〒150-0074
東京都渋谷区桜見台7-13-6朝陽ビル
TEL:03-6928-4171(代)
FAX:03-6928-4178

西日本支社
大阪事務所
〒530-0086
大阪府大阪市北区松風町 6-3-18 青葉セントラルビル
TEL:06-6384-2051
FAX:06-6384-2052

西日本支社
広島事務所
〒730-0094
広島県広島市中区千草通3-8-12浜辺ビル5F
TEL:082-517-6820
FAX:082-517-6829
A4
両面
赤系、緑系、水色系
• 高解像度JPG (.jpg)
• イラストレーター形式 (.ai)
使用可能な画像、図(こちらもチラシ作成上に入れてほしいがわかりやすくいじってもらってOKです)、会社ロゴ等全て添付します。

業界関係者ではなく、一般のかた(いわゆる「素人」)が、パッとみてどう感じるだろうか、という
目線で選定しました。
・あまり小難しい印象は与えず、明快なデザイン
・「マンション販売のチラシ」や「水道修理業者」と勘違いされない
というようなところで差がありました。

はじめてこのワークバザールを利用したのですが、このように色々なご提案をいただき、
正直、驚き(もちろん嬉しい方です)でした。
やはりプロにお任せするだけのことがあると痛感し、
我々の業務も同じような驚きをお客様にお届けできるように心がけたいと思います。

この度はご提案いただきまして、誠にありがとうございました。

```html
<!DOCTYPE html>
<html lang="ja">
<head>
<meta charset="UTF-8">
<title>うちのマンション 耐用年数 あとどれくらい？</title>
<link href="https://fonts.googleapis.com/css2?family=Noto+Sans+JP:wght@400;500;700;900&display=swap" rel="stylesheet">
<style>
  :root {
    --ink: #111111;
    --paper: #ffffff;
    --accent-red: #d8232a;
    --bubble-line: #333333;
    --people-tone: #c9d6e4;
    --people-tone-2: #e8d7c4;
    --building-tone: #d9d2c2;
    --building-tone-2: #9fc4d9;
  }
  * { margin: 0; padding: 0; box-sizing: border-box; }
  html, body { width: 854px; height: 1200px; overflow: hidden; background: var(--paper); }
  body { font-family: "Noto Sans JP", sans-serif; color: var(--ink); }
  .flyer { position: relative; width: 854px; height: 1200px; background: var(--paper); }

  .headline-top {
    position: absolute; top: 14px; left: 0; width: 100%;
    text-align: center; font-weight: 900; font-size: 98px; letter-spacing: 1px; line-height: 1.2;
  }

  .bubble { position: absolute; font-size: 15px; font-weight: 500; line-height: 1.5; }
  .bubble svg { position: absolute; inset: 0; width: 100%; height: 100%; overflow: visible; }
  .bubble p { position: relative; padding: 20px 0 0; text-align: center; white-space: nowrap; }
  .bubble-owner { left: 50px; top: 165px; width: 240px; height: 118px; }
  .bubble-engineer { left: 308px; top: 175px; width: 226px; height: 100px; }
  .bubble-resident { left: 552px; top: 165px; width: 262px; height: 118px; }

  .people { position: absolute; top: 290px; height: 250px; border-radius: 40% 40% 6px 6px; }
  .people-owner { left: 95px; width: 180px; background: linear-gradient(180deg, var(--people-tone-2), var(--people-tone)); }
  .people-engineer { left: 340px; width: 170px; background: linear-gradient(180deg, var(--people-tone-2), #e6ebf2); }
  .people-resident { left: 590px; width: 175px; background: linear-gradient(180deg, #d8b98f, #f2c5c0); }

  .headline-main {
    position: absolute; top: 545px; left: 0; width: 100%;
    text-align: center; font-weight: 900; font-size: 186px; letter-spacing: 2px; line-height: 1.1;
  }

  .building-illustration {
    position: absolute; left: 85px; top: 775px; width: 305px; height: 200px;
    background: linear-gradient(160deg, var(--building-tone-2), var(--building-tone) 70%, #b7cf9a);
    border-radius: 8px;
  }

  .appeal { position: absolute; left: 420px; top: 768px; width: 410px; }
  .appeal-lead { font-size: 21px; font-weight: 500; }
  .appeal-service {
    display: inline-block; margin-top: 10px; padding: 4px 8px;
    border: 2px solid var(--accent-red); font-size: 25px; font-weight: 700; color: var(--accent-red); white-space: nowrap;
  }
  .appeal-service small { font-size: 15px; }
  .appeal-call { margin-top: 8px; font-size: 21px; font-weight: 500; }

  .points { position: absolute; left: 410px; top: 920px; width: 420px; list-style: none; font-size: 16px; line-height: 1.65; }
  .points li { padding-left: 1em; text-indent: -1em; margin-bottom: 6px; }
  .points li::before { content: "・"; }

  .headline-bottom {
    position: absolute; top: 1060px; left: 0; width: 100%;
    text-align: center; font-weight: 900; font-size: 96px; letter-spacing: 1px; line-height: 1.2;
  }
</style>
</head>
<body>
<main class="flyer">
  <h1 class="headline-top">うちのマンション</h1>

  <div class="bubble bubble-owner">
    <svg viewBox="0 0 240 118" preserveAspectRatio="none"><path d="M120 4 C218 4 236 30 236 56 C236 86 208 106 130 106 L122 116 L110 105 C32 104 4 86 4 56 C4 26 32 4 120 4Z" fill="#fff" stroke="var(--bubble-line)" stroke-width="2"/></svg>
    <p>2年後には築30年。次の<br>大規模修繕はどんな方<br>針でいこうか？</p>
  </div>
  <div class="bubble bubble-engineer">
    <svg viewBox="0 0 226 100" preserveAspectRatio="none"><path d="M113 4 C204 4 222 26 222 48 C222 74 194 90 123 90 L113 99 L104 90 C32 90 4 74 4 48 C4 24 26 4 113 4Z" fill="#fff" stroke="var(--bubble-line)" stroke-width="2"/></svg>
    <p>修繕、改修か？建替えも<br>視野に入れるか？ですね。</p>
  </div>
  <div class="bubble bubble-resident">
    <svg viewBox="0 0 262 118" preserveAspectRatio="none"><path d="M131 4 C236 4 258 28 258 56 C258 86 230 106 141 106 L133 116 L123 106 C36 106 4 86 4 56 C4 26 30 4 131 4Z" fill="#fff" stroke="var(--bubble-line)" stroke-width="2"/></svg>
    <p>それなら、建物の寿命が<br>あとどのくらい残っているか<br>ぜひ知りたいわね。</p>
  </div>

  <div class="people people-owner" role="img" aria-label="修繕方針を考える年配の男性のイラスト"></div>
  <div class="people people-engineer" role="img" aria-label="資料を持った男性のイラスト"></div>
  <div class="people people-resident" role="img" aria-label="話し合いに加わる女性のイラスト"></div>

  <h2 class="headline-main">耐用年数</h2>

  <div class="building-illustration" role="img" aria-label="マンション建物のイラスト"></div>

  <div class="appeal">
    <p class="appeal-lead">将来のリスク回避のために</p>
    <p class="appeal-service">マンション<small>向け</small>建物耐用年数評価</p>
    <p class="appeal-call">を受けましょう</p>
  </div>

  <ul class="points">
    <li>建物（鉄筋（鉄骨）コンクリート躯体）の寿命が、あとどれくらい残っているのか（＝寿命）を評価する――それが「建物耐用年数評価」です。</li>
    <li>いまお住まいのマンションの、将来計画を考えるために重要な基礎資料となります。</li>
  </ul>

  <p class="headline-bottom">あとどれくらい？</p>
</main>
</body>
</html>
```